Velvet Oaks rebranding my business with a new business card

I have my new logo and now I need a refresher on my business cards. I really want something fun and fresh. I like black background or anything to make the color pop.
Logo
Name: Velvet Oaks
Contact Info as stated below:
Mira Calloway
647-382-9164
Logo
Name: Velvet Oaks
Mira Calloway
647-382-9164
fb.me/VelvetOaksbyMira
Instagram: @VelvetOaksbyMira

Industry/Entity Type

Business

Contact Information for Business Card

double-sided. Logo on one side. Contact info on the other.

Requirements
Must have
• Logo
• Name: Velvet Oaks
• Contact Info as stated below:
• Mira Calloway
• 647-382-9164
• fb.me/VelvetOaksbyMira
• fb.me/VelvetOaksbyMira

```html
<!DOCTYPE html>
<html lang="en">
<head>
<meta charset="utf-8">
<title>Velvet Oaks – Business Card</title>
<link rel="stylesheet" href="https://fonts.googleapis.com/css2?family=Enriqueta:wght@400;500&family=Poppins:wght@400;500&display=swap">
<style>
  :root {
    --backdrop: #1f1f1f;
    --card-white: #ffffff;
    --pink: #f09fae;
    --pink-deep: #ef97a8;
    --pink-ring: #f3b3c0;
    --teal: #1fa596;
    --ink: #3a3a3a;
  }
  * { margin: 0; padding: 0; box-sizing: border-box; }
  html, body {
    width: 1200px; height: 897px; overflow: hidden;
    background: var(--backdrop);
  }
  .stage { position: relative; width: 1200px; height: 897px; }

  .card {
    position: absolute; left: 341px; width: 506px;
    border-radius: 11px; overflow: hidden;
    background: var(--card-white);
  }
  .card--front { top: 154px; height: 290px; background: var(--pink); }
  .card--back  { top: 464px; height: 286px; }

  .front__band {
    position: absolute; left: 0; top: 94px; width: 100%; height: 102px;
    background: var(--card-white);
  }
  .front__pattern {
    position: absolute; left: 0; width: 100%; height: 94px;
    background: linear-gradient(180deg, #f2a4b2, #ee9aaa);
  }
  .front__pattern--top { top: 0; }
  .front__pattern--bottom { top: 196px; }

  .seal {
    position: absolute; border-radius: 50%;
    background: var(--card-white);
    border: 2px solid var(--ink);
    display: flex; align-items: center; justify-content: center;
  }
  .seal::before {
    content: ""; position: absolute; inset: 4px;
    border-radius: 50%; border: 2px solid var(--pink-ring);
  }
  .seal__name {
    font-family: "Poppins", sans-serif; font-weight: 500;
    color: var(--teal); text-align: center; line-height: 1.15;
  }
  .card--front .seal { left: 173px; top: 63px; width: 162px; height: 162px; }
  .card--front .seal__name { font-size: 20px; }

  .back__stripe {
    position: absolute; left: 58px; top: 0; width: 104px; height: 100%;
    background: var(--pink-deep);
  }
  .card--back .seal { left: 36px; top: 70px; width: 148px; height: 148px; }
  .card--back .seal__name { font-size: 18px; }

  .contact {
    position: absolute; left: 254px; top: 78px; width: 200px;
    text-align: center;
  }
  .contact__name {
    font-family: "Enriqueta", serif; font-weight: 500;
    font-variant: small-caps; letter-spacing: 2px;
    font-size: 26px; color: var(--teal); line-height: 1; white-space: nowrap;
  }
  .contact__rule {
    width: 20px; height: 2px; background: var(--teal);
    margin: 12px auto 14px;
  }
  .contact__lines {
    list-style: none;
    font-family: "Poppins", sans-serif; font-size: 12.5px;
    color: var(--ink); line-height: 20.5px; white-space: nowrap;
  }
</style>
</head>
<body>
<main class="stage">
  <section class="card card--front" aria-label="Card front">
    <div class="front__pattern front__pattern--top" role="img" aria-label="Faint pattern of ice creams and popsicles on pink"></div>
    <div class="front__band"></div>
    <div class="front__pattern front__pattern--bottom" role="img" aria-label="Faint pattern of ice creams and popsicles on pink"></div>
    <div class="seal"><span class="seal__name">Velvet<br>Oaks</span></div>
  </section>

  <section class="card card--back" aria-label="Card back">
    <div class="back__stripe"></div>
    <div class="seal"><span class="seal__name">Velvet<br>Oaks</span></div>
    <div class="contact">
      <h1 class="contact__name">Mira Calloway</h1>
      <div class="contact__rule"></div>
      <ul class="contact__lines">
        <li>647-382-9164</li>
        <li>info@miracalloway.com</li>
        <li>fb: me/VelvetOaksbyMira</li>
        <li>ins: @VelvetOaksbyMira</li>
      </ul>
    </div>
  </section>
</main>
</body>
</html>
```